Business Card Design Project

we are a new company , see www.chatharborlane.com
we also have a concurrent flyer deign competition so you may also wish to enter that.
We provide live customer support services for websites.
We cater for mainly european market.
info for card:
Martin Colbrook
Director
p: +353 (0)90 612 8051
f: +353 (0)90 612 8062
m: +353 (0)86 507 4926
e: martin@chatharborlane.com
w: www.chatharborlane.com
The card does not have to use the exact colour on the website but should ahve something of the general feel of it. It should have modern corporate feel without brash coulours. we will upload the logo and card should be standard european size 85x55mm
Target Market(s)
Online business owners
Industry/Entity Type
Business
Look and feel
Each slider illustrates characteristics of the customer's brand and the style your logo design should communicate.

```html
<!DOCTYPE html>
<html lang="en">
<head>
<meta charset="utf-8">
<title>Chat Harbor Lane – Business Card</title>
<link rel="stylesheet" href="https://fonts.googleapis.com/css2?family=Roboto:wght@400;700&display=swap">
<style>
  :root {
    --page-bg: #e6e6e6;
    --card-dark: #4a4a4a;
    --card-light: #ffffff;
    --brand-blue: #1f8fd0;
    --text-grey: #555555;
    --text-light: #ffffff;
    --mark-grey: #5a5a5a;
  }
  * { box-sizing: border-box; margin: 0; padding: 0; }
  html, body {
    width: 1200px; height: 828px; overflow: hidden;
    background: var(--page-bg);
    font-family: "Roboto", Arial, sans-serif;
  }
  .canvas {
    position: relative; width: 1200px; height: 828px;
    display: flex; align-items: center; justify-content: center; gap: 60px;
  }
  .card {
    position: relative; width: 520px; height: 336px;
    border-radius: 26px;
    box-shadow: 0 8px 24px rgba(0,0,0,.18);
  }
  .card-back { background: var(--card-dark); }
  .card-front { background: var(--card-light); }

  .wordmark {
    position: absolute; display: flex; align-items: center; gap: 10px;
    font-weight: 700; white-space: nowrap;
  }
  .wordmark-square { width: 22px; height: 22px; background: var(--brand-blue); }
  .card-back .wordmark {
    left: 50%; top: 128px; transform: translateX(-50%);
    font-size: 38px; color: var(--text-light);
  }
  .card-back .website {
    position: absolute; right: 52px; bottom: 46px;
    font-size: 13px; color: var(--text-light);
  }

  .card-front .wordmark {
    left: 40px; top: 172px; font-size: 26px; color: var(--mark-grey);
  }
  .card-front .wordmark-square { width: 16px; height: 16px; }
  .contact {
    position: absolute; left: 292px; top: 70px; color: var(--text-grey);
  }
  .contact-name { font-size: 21px; color: var(--brand-blue); }
  .contact-role { font-size: 15px; margin-top: 4px; }
  .contact-list { list-style: none; margin-top: 28px; font-size: 14px; line-height: 21px; }
  .contact-label { display: inline-block; width: 18px; color: var(--brand-blue); }
</style>
</head>
<body>
<main class="canvas">
  <section class="card card-back" aria-label="Card back">
    <div class="wordmark"><span class="wordmark-square"></span>Chat Harbor Lane</div>
    <p class="website">www.chatharborlane.com</p>
  </section>

  <section class="card card-front" aria-label="Card front">
    <div class="wordmark"><span class="wordmark-square"></span>Chat Harbor Lane</div>
    <div class="contact">
      <p class="contact-name">Martin Colbrook</p>
      <p class="contact-role">Director</p>
      <ul class="contact-list">
        <li><span class="contact-label">p</span>+353 (0)90 612 8051</li>
        <li><span class="contact-label">f</span>+353 (0)90 612 8062</li>
        <li><span class="contact-label">m</span>+353 (0)86 507 4926</li>
        <li><span class="contact-label">e</span>martin@chatharborlane.com</li>
        <li><span class="contact-label">w</span>www.chatharborlane.com</li>
      </ul>
    </div>
  </section>
</main>
</body>
</html>
```